Hautglanz Kosmetik Göttingen sucht Werbeplakat für Außenwerbung
Zielgruppe
Wir sind ein junges modernes Kosmetikstudio im Herzen der Studentenstadt Göttingen.
Wir bieten allen Zielgruppen ein attraktives Preisleistungsverhältnis.
http://www.hautglanz-kosmetik.example/
Aufgabenstellung
Wir benötigen für ein großes Außenplakat eine ansprechende Werbung für unser Studio.
Schwerpunkt sollte dabei unser Angebot für dauerhafte Haarentfernung mittels IPL Technologie sein.
Es soll optisch ansprechend sein (eye catcher) und auch Studenten ansprechen.

```html
<!DOCTYPE html>
<html lang="de">
<head>
<meta charset="utf-8">
<title>Hautglanz Kosmetik – Dauerhafte Haarentfernung</title>
<link href="https://fonts.googleapis.com/css2?family=PT+Sans:wght@400;700&family=Kalam:wght@300;400&display=swap" rel="stylesheet">
<style>
  :root {
    --purple: #48227a;
    --white: #ffffff;
    --headline: rgba(235, 228, 230, 0.72);
    --skin-light: #b9795a;
    --skin-mid: #8a5240;
    --skin-dark: #4b2e2e;
    --backdrop: #5a4c55;
  }
  * { margin: 0; padding: 0; box-sizing: border-box; }
  html, body { width: 848px; height: 1200px; overflow: hidden; background: var(--purple); }
  .poster {
    position: relative; width: 848px; height: 1200px; overflow: hidden;
    background: var(--purple);
    font-family: "PT Sans", sans-serif;
  }
  .hero-photo {
    position: absolute; left: 0; top: 0; width: 848px; height: 918px;
    background:
      radial-gradient(ellipse 38% 30% at 42% 28%, var(--skin-light), transparent 70%),
      radial-gradient(ellipse 30% 42% at 62% 60%, #a8684e, transparent 72%),
      radial-gradient(ellipse 26% 40% at 30% 62%, #9a5c46, transparent 72%),
      radial-gradient(ellipse 60% 70% at 50% 50%, var(--skin-mid), transparent 80%),
      linear-gradient(90deg, var(--backdrop), var(--skin-dark) 30%, var(--skin-dark) 70%, var(--backdrop));
  }
  .headline {
    position: absolute; left: 48px; top: 140px;
    font-weight: 700; font-size: 171px; line-height: 171px;
    color: var(--headline); letter-spacing: -3px;
  }
  .subline {
    position: absolute; left: 52px; top: 664px;
    color: var(--white); font-size: 42px; line-height: 55px;
  }
  .promise {
    position: absolute; left: 515px; top: 800px; width: 360px; height: 168px;
    background: var(--purple);
    border-top: 4px solid var(--white); border-bottom: 4px solid var(--white);
    transform: rotate(-6deg); transform-origin: left top;
    box-shadow: -2px 3px 6px rgba(0,0,0,0.35);
  }
  .promise p {
    position: absolute; left: 22px; top: 10px; width: 320px;
    font-family: "Kalam", cursive; font-weight: 300;
    color: var(--white); font-size: 22px; line-height: 28px;
  }
  .contact {
    position: absolute; left: 52px; top: 1012px;
    color: var(--white); font-size: 20px; line-height: 29px;
  }
  .contact .phone { font-weight: 700; }
  .brand {
    position: absolute; left: 448px; top: 1012px; width: 352px; color: var(--white);
  }
  .brand-name { font-weight: 700; font-size: 50px; line-height: 56px; }
  .brand-tagline { font-size: 24px; line-height: 32px; margin-top: 6px; }
  .brand-services { font-size: 14px; line-height: 22px; margin-top: 4px; }
</style>
</head>
<body>
<main class="poster">
  <div class="hero-photo" role="img" aria-label="Foto einer Person mit glatter Haut, sitzend mit angezogenen Knien, in warmen Hauttönen"></div>

  <h1 class="headline">Das gibt<br>&#180;ne glatte<br>1,0.</h1>

  <p class="subline">Dauerhafte Haarentfernung<br>mittels IPL Technologie</p>

  <div class="promise">
    <p>Wir sind auf dauerhafte Haarentfernung spezialisiert. Lassen Sie sich gern von uns persönlich beraten.</p>
  </div>

  <address class="contact" style="font-style:normal">
    Lindenhofweg 14 (1. OG)<br>
    37073 Göttingen<br>
    <span class="phone">Tel. : 0551 4417308</span><br>
    email@hautglanz-kosmetik.example<br>
    http://www.hautglanz-kosmetik.example
  </address>

  <div class="brand">
    <div class="brand-name">Hautglanz</div>
    <div class="brand-tagline">Dein Kosmetikstudio in Göttingen</div>
    <div class="brand-services">Dauerhafte Haarentfernung • Kosmetik • Naildesign • Fußpflege</div>
  </div>
</main>
</body>
</html>
```